Email Sig, Letterhead, Business Card Design

Need a stationary package including email signature, letterhead/envelope, and business card design incorporating our new logo.

```html
<!DOCTYPE html>
<html lang="en">
<head>
<meta charset="utf-8">
<title>Corvan Engineering – Business Card</title>
<link rel="stylesheet" href="https://fonts.googleapis.com/css2?family=Libre+Baskerville:wght@700&family=Mulish:wght@300;400;800&display=swap">
<style>
  :root {
    --bg: #e9e7e4;
    --card-dark: #2b2b2d;
    --card-dark-deep: #0e0e10;
    --card-light: #e2e1df;
    --card-light-edge: #cfcdca;
    --navy: #14295a;
    --red: #c2231c;
    --text-light: #ededed;
    --text-muted: #cfcfcf;
  }
  html, body {
    margin: 0;
    width: 1200px;
    height: 969px;
    overflow: hidden;
    background: var(--bg);
  }
  .card {
    position: absolute;
    left: 100px;
    top: 200px;
    width: 1000px;
    height: 570px;
    border-radius: 26px;
    overflow: hidden;
    background: radial-gradient(ellipse at 75% 55%, #f1f0ee 0%, var(--card-light) 55%, var(--card-light-edge) 100%);
    box-shadow: 0 10px 30px rgba(0,0,0,0.18);
  }
  .card-art {
    position: absolute;
    inset: 0;
  }
  .contact {
    position: absolute;
    left: 41px;
    top: 118px;
    color: var(--text-light);
    font-family: "Mulish", sans-serif;
    font-weight: 300;
  }
  .contact .name {
    margin: 0;
    font-family: "Libre Baskerville", serif;
    font-weight: 700;
    font-size: 31px;
    letter-spacing: 0.3px;
    line-height: 40px;
  }
  .contact .title {
    margin: 0;
    font-size: 21px;
    line-height: 26px;
    color: var(--text-muted);
  }
  .contact .address {
    margin: 38px 0 0;
    font-size: 21px;
    line-height: 28px;
    font-style: normal;
  }
  .contact .lines {
    list-style: none;
    margin: 16px 0 0;
    padding: 0;
  }
  .contact .lines li {
    display: flex;
    align-items: center;
    font-size: 22px;
    line-height: 28.5px;
  }
  .contact .lines svg {
    width: 18px;
    height: 18px;
    margin: 0 14px 0 0;
    fill: var(--text-light);
    flex: none;
  }
  .brand {
    position: absolute;
    left: 530px;
    width: 400px;
    top: 180px;
    text-align: center;
  }
  .brand .mark {
    width: 96px;
    height: 96px;
    margin: 0 auto 48px;
    border-radius: 50%;
    background: var(--navy);
  }
  .brand .company {
    margin: 0;
    font-family: "Libre Baskerville", serif;
    font-weight: 700;
    font-size: 30px;
    line-height: 36px;
    color: var(--red);
    white-space: nowrap;
  }
  .brand .street {
    margin: 4px 0 0;
    font-family: "Mulish", sans-serif;
    font-weight: 800;
    font-size: 13px;
    letter-spacing: -0.2px;
    color: var(--navy);
    white-space: nowrap;
  }
  .brand .registration {
    display: flex;
    align-items: center;
    gap: 8px;
    margin: 3px 0 0;
    font-family: "Mulish", sans-serif;
    font-weight: 800;
    font-size: 11px;
    letter-spacing: 2px;
    color: var(--red);
    white-space: nowrap;
  }
  .brand .registration::before,
  .brand .registration::after {
    content: "";
    flex: 1;
    height: 2px;
    background: var(--red);
  }
</style>
</head>
<body>
  <section class="card">
    <svg class="card-art" viewBox="0 0 1000 570" width="1000" height="570" aria-hidden="true">
      <defs>
        <radialGradient id="darkPanel" cx="0.35" cy="0.55" r="0.75">
          <stop offset="0" stop-color="#3a3a3c"/>
          <stop offset="1" stop-color="#0f0f11"/>
        </radialGradient>
      </defs>
      <path class="swoosh-red" fill="#c2231c" d="M0,0 H568 C596,72 566,155 514,232 C446,340 444,468 590,570 H0 Z"/>
      <path class="swoosh-gap" fill="#f4f3f1" d="M0,0 H562 C588,68 558,150 505,228 C436,338 434,468 574,570 H0 Z"/>
      <path class="swoosh-navy" fill="#14295a" d="M0,0 H558 C582,66 552,146 498,226 C428,336 426,468 566,570 H0 Z"/>
      <path class="panel-dark" fill="url(#darkPanel)" d="M0,0 H548 C570,60 540,140 484,220 C408,330 410,470 540,570 H0 Z"/>
      <path class="panel-edge" fill="none" stroke="#d9d9d9" stroke-width="1.2" d="M548,0 C570,60 540,140 484,220 C408,330 410,470 540,570"/>
    </svg>

    <div class="contact">
      <h1 class="name">Daniel Reyes</h1>
      <p class="title">President</p>
      <address class="address">412 Alder Street<br>Fairview, Oregon 55102</address>
      <ul class="lines">
        <li><svg viewBox="0 0 24 24"><path d="M6.6 10.8a15.1 15.1 0 0 0 6.6 6.6l2.2-2.2a1 1 0 0 1 1-.25 11.4 11.4 0 0 0 3.6.57 1 1 0 0 1 1 1V20a1 1 0 0 1-1 1A17 17 0 0 1 3 4a1 1 0 0 1 1-1h3.5a1 1 0 0 1 1 1c0 1.25.2 2.45.57 3.57a1 1 0 0 1-.25 1z"/></svg>555-210-4836</li>
        <li><svg viewBox="0 0 24 24"><path d="M7 1h10a2 2 0 0 1 2 2v18a2 2 0 0 1-2 2H7a2 2 0 0 1-2-2V3a2 2 0 0 1 2-2zm0 3v14h10V4zm5 15.5a1 1 0 1 0 0 2 1 1 0 0 0 0-2z"/></svg>555-348-9172</li>
        <li><svg viewBox="0 0 24 24"><path d="M6 2h12v6H6zM3 9h18a2 2 0 0 1 2 2v7h-4v4H5v-4H1v-7a2 2 0 0 1 2-2zm4 7v4h10v-4z"/></svg>555-627-0419</li>
        <li><svg viewBox="0 0 24 24"><path d="M2 5h20v14H2zm2 2v.5l8 5 8-5V7zm0 3v7h16v-7l-8 5z"/></svg>hello@corvaneng.com</li>
        <li><svg viewBox="0 0 24 24"><path d="M12 2a10 10 0 1 0 0 20 10 10 0 0 0 0-20zm-1 17.9A8 8 0 0 1 4.1 10L9 15v1a2 2 0 0 0 2 2zm6.9-2.5A2 2 0 0 0 16 16h-1v-3a1 1 0 0 0-1-1H8v-2h2a1 1 0 0 0 1-1V7h2a2 2 0 0 0 2-2v-.4a8 8 0 0 1 2.9 12.8z"/></svg>corvaneng.com</li>
      </ul>
    </div>

    <div class="brand">
      <div class="mark"></div>
      <p class="company">CORVAN ENGINEERING</p>
      <p class="street">1480 CEDAR RIDGE ROAD, LINWOOD, TEXAS 75310</p>
      <p class="registration">STATE FIRM REGISTRATION F-4812</p>
    </div>
  </section>
</body>
</html>
```